The Band is called ''Lantern Hollow'' and the Album is called ''Quiet Harbor''.
The recording was done in Malibu CA with a famous producer Martin Pelloway. The style of music is rock pop, Ned Farrow style.

The concept for the album cover is based on a song ''Quiet Harbor'' which is listed on the album. We are all seeking a Quiet Harbor and if you can't find a Quiet Harbor then make it one for yourself.
The song gives you a sense of hope.

My idea is very simple as the music is very organic and stripped back and clean. The front and back cover is pure white; On the front is a whole orange which is starting to grow greenish mould on it. The mouldy orange has a cocktail umbrella stabbed in the side of it - this suggests that the fruit itself has had better days.I would also like on the orange countries/ continents- (Australia and Tasmania must feature). The countries should be clear and crisp and as they progressively reach the mould they merge into the mouldy part of the orange (the ocean would be the orange colour) never to be seen. World decaying like fruit.
On the back of the album would be a fresh dewy full orange with the same cocktail umbrella sticking out of it with the continents/ countries of the world

The printed image on the disc itself would be a 1/2 cut orange so its like a circle of orange.

I realise its very simple but it could be very effective like the Tamsk album cover - ''the paper moth'' where they have a full egg and inside the cover the whole egg shell is now cracked.

Looking forward to your ideas!
Rosalind

Requirements
Must have
• Song list on back;
1. Drifting Slowly
2. Too Late ( The Lantern Tune)
3. Quiet Harbor
4. Keep It Near
5. Worn Maps
6. Hey Hold Still
7. Tides 4
8. Turn and Run
9. Seven Locks
10. Follow Home
11. Undertowed
12. Velvet Static

Produced by; Martin Pelloway- ''Tin Kettle Recordings'' Malibu, California, USA.

```html
<!DOCTYPE html>
<html lang="en">
<head>
<meta charset="utf-8">
<title>Lantern Hollow — Quiet Harbor disc label</title>
<link rel="stylesheet" href="https://fonts.googleapis.com/css2?family=Libre+Baskerville:wght@700&display=swap">
<style>
  :root {
    --paper: #ffffff;
    --rind-outer: #f3b21f;
    --rind-inner: #f9d349;
    --pith: #fbe08a;
    --flesh-light: #f9922a;
    --flesh-deep: #ee7412;
    --ink-dark: #262626;
    --ink-light: #ffffff;
  }
  html, body {
    margin: 0;
    padding: 0;
    overflow: hidden;
    background: var(--paper);
  }
  .canvas {
    position: relative;
    width: 1199px;
    height: 1200px;
    background: var(--paper);
    overflow: hidden;
  }
  .disc-label {
    position: absolute;
    inset: 0;
    display: block;
  }
  .label-text {
    font-family: "Libre Baskerville", "Times New Roman", serif;
    font-weight: 700;
    text-anchor: middle;
  }
  .band-name {
    fill: var(--ink-dark);
    font-size: 54px;
    letter-spacing: -1px;
  }
  .album-title {
    fill: var(--ink-light);
    font-size: 78px;
    letter-spacing: -1px;
  }
</style>
</head>
<body>
  <main class="canvas">
    <svg class="disc-label" viewBox="0 0 1199 1200" width="1199" height="1200" xmlns="http://www.w3.org/2000/svg">
      <defs>
        <radialGradient id="slice-flesh" cx="50%" cy="50%" r="50%">
          <stop offset="0%" stop-color="var(--flesh-light)"/>
          <stop offset="60%" stop-color="var(--flesh-deep)"/>
          <stop offset="88%" stop-color="var(--flesh-light)"/>
          <stop offset="93%" stop-color="var(--pith)"/>
          <stop offset="97%" stop-color="var(--rind-inner)"/>
          <stop offset="100%" stop-color="var(--rind-outer)"/>
        </radialGradient>
        <mask id="spindle-hole">
          <rect width="1199" height="1200" fill="#fff"/>
          <circle cx="600" cy="600" r="195" fill="#000"/>
        </mask>
      </defs>

      <g class="orange-slice" role="img" aria-label="Photograph of a halved orange seen from above, juicy segments radiating from the centre with a yellow rind">
        <circle cx="600" cy="600" r="597" fill="url(#slice-flesh)" mask="url(#spindle-hole)"/>
      </g>

      <text class="label-text band-name" x="600" y="332">LANTERN HOLLOW</text>
      <text class="label-text album-title" x="600" y="968">QUIET HARBOR</text>
    </svg>
  </main>
</body>
</html>
```